依頼概要
■ 依頼の目的/概要

新しくオープンする通販サイトの宣伝用チラシの制作をお願い致します。

【サイトについて】

○サイト名
TR472
TeleRelay472の略で、コールセンターの119番という意味合いです。

○取り扱い商材
ヘッドセット、IP電話など(主に法人のお客様向けです)

○特色
・ ヘッドセットの取り扱いメーカー数が多いこと
・ 扱う商材が幅広い(ヘッドセットだけでなく、IP電話等も取り扱う)こと

【盛り込んで頂きたいメッセージ】

①TR472というサイトがオープンしました、ということ
②1~2台の小規模な購入でいちいち見積もりをとって購入するのは面倒
といった方をレスキューするサイトです、ということ

【チラシのターゲット】
コールセンター(お客様相談窓口など)で、ヘッドセット等機器の購入を任されている担当者
(男性の方も、女性の方もいらっしゃいます)

【チラシの体裁】
A41枚

■ デザインへの要望

・パッと人目を引く、インパクトのあるデザイン
・情報がわかりやすくまとめられているもの

※当サイトのロゴ、取り扱いメーカーのロゴ、商品画像、サイトのTOPページ画像
などを添付致しますので、ご活用いただきたいと思います。

■ 納品ファイルの希望

「.png」形式

■ 利用用途

営業用チラシほか、当サイト全ての広告活動に利用します。

■ 進め方

弊社の希望するイメージに近い提案を1つ(場合によって複数)選択させて頂きます。希望に近づけるために、修正要望を個別にさせて頂くこともあります。コンペ方式のため、修正後に当選されない場合も、どうかご了承ください。

■ その他/注意点

選択させて頂いたデザインの著作権(財産権)等の扱いはHirakus利用規約に従い、弊社に譲渡をお願いします。フォントや画像素材などを利用する場合は上記利用用途に使用できることを確認し、第三者の知的財産権等に注意して下さい。
<2010/06/17追記>

入れ込んで欲しいマスト情報として、
サイトURL、FAX/TEL番号を追加させて頂きます。

```html
<!DOCTYPE html>
<html lang="ja">
<head>
<meta charset="utf-8">
<title>TeleRelay472 オープン告知チラシ</title>
<link rel="stylesheet" href="https://fonts.googleapis.com/css2?family=Noto+Sans+JP:wght@400;700;900&display=swap">
<style>
  :root{
    --red:#e60012;
    --blue:#0a3f9c;
    --blue-mid:#1f6fd1;
    --blue-pale:#dbe9f8;
    --orange:#f08300;
    --ink:#1a1a1a;
    --white:#ffffff;
  }
  *{margin:0;padding:0;box-sizing:border-box}
  html,body{width:847px;height:1200px;overflow:hidden;background:var(--white)}
  body{font-family:"Noto Sans JP",sans-serif;color:var(--ink)}
  .flyer{position:relative;width:847px;height:1200px;overflow:hidden;
    background:linear-gradient(180deg,var(--white) 0%,var(--white) 55%,#eef4fb 100%)}

  .site-preview{position:absolute;left:14px;top:8px;width:520px;height:272px;
    transform:rotate(-2deg);border:3px solid #c9d3df;
    background:linear-gradient(160deg,#f4f7fb 0%,#c9dbef 45%,#7fa6d6 100%);
    box-shadow:3px 4px 8px rgba(0,0,0,.25)}
  .sticker-space{position:absolute;left:556px;top:22px;width:279px;height:84px;
    background:var(--white);border:2px solid #999;display:flex;align-items:center;
    justify-content:center;font-size:24px;font-weight:700;letter-spacing:1px}

  .products{position:absolute;left:20px;top:290px;display:flex;gap:8px}
  .products li{list-style:none;background:var(--red);color:var(--white);
    font-weight:700;font-size:19px;padding:2px 10px;border-radius:3px;line-height:28px}

  .kicker{position:absolute;left:0;width:100%;top:318px;text-align:center;
    color:var(--red);font-weight:900;font-size:54px;letter-spacing:1px;
    -webkit-text-stroke:2px var(--white);paint-order:stroke fill}
  .site-name{position:absolute;left:0;width:100%;top:392px;text-align:center;
    color:var(--blue);font-weight:900;font-size:88px;line-height:100px;letter-spacing:-1px}
  .headline{position:absolute;left:0;width:100%;top:496px;text-align:center;
    color:var(--red);font-weight:900;font-size:100px;line-height:116px;letter-spacing:2px}
  .lead{position:absolute;right:40px;top:620px;color:var(--blue);font-weight:700;font-size:23px}

  .rescue-band{position:absolute;left:0;top:672px;width:847px;height:36px;
    background:linear-gradient(90deg,var(--blue-mid) 0%,var(--blue-pale) 60%,transparent 100%);
    display:flex;align-items:center}
  .rescue-band p{margin-left:34px;color:var(--blue);font-weight:700;font-size:20px;
    background:var(--white);padding:0 8px;border-radius:2px}

  .worries{position:absolute;left:26px;top:722px;width:490px;list-style:none}
  .worries li{position:relative;padding-left:30px;font-weight:700;font-size:27px;
    line-height:40px;margin-bottom:22px}
  .worries li::before{content:"";position:absolute;left:0;top:10px;width:22px;height:22px;
    background:var(--blue-mid)}
  .worries em{font-style:normal;color:var(--blue-mid)}

  .campaign{position:absolute;left:530px;top:745px;width:300px;text-align:center}
  .campaign .sale{color:var(--orange);font-weight:900;font-size:34px;line-height:44px}
  .campaign .offer{margin-top:18px;color:var(--blue);font-weight:900;font-size:40px;line-height:56px}
  .campaign .offer strong{color:var(--red);font-size:50px}
  .campaign .more{margin-top:24px;color:var(--blue);font-weight:900;font-size:28px}
</style>
</head>
<body>
<main class="flyer">
  <div class="site-preview" role="img" aria-label="通販サイトのトップページ画面"></div>
  <div class="sticker-space">シールスペース</div>

  <ul class="products">
    <li>ヘッドセット</li>
    <li>通話録音機器</li>
    <li>ヘッドセット型電話機</li>
    <li>IP電話機</li>
    <li>etc...</li>
  </ul>

  <p class="kicker">コールセンター通販サイト</p>
  <h1 class="site-name">TeleRelay472</h1>
  <p class="headline">待望のオープン!!</p>
  <p class="lead">TR472では、国内のヘッドセットメーカーを網羅しています!</p>

  <div class="rescue-band"><p>TR472はこんな方をレスキューするサイトです!</p></div>

  <ul class="worries">
    <li><em>あちこちのサイト</em>を見て製品を<br>比較するのは疲れる…</li>
    <li><em>小規模な購入</em>でもいちいち<br>見積もりをとるのは面倒…</li>
    <li><em>新商品などのニュース</em>は<br>早く知りたい!</li>
    <li><em>もっとスピーディー</em>に<br>お買い物をしたい!</li>
  </ul>

  <section class="campaign">
    <p class="sale">オープンセール<br>実施中!</p>
    <p class="offer">先着300名様に<br><strong>2000</strong>円分の商品券<br>をプレゼント!!</p>
    <p class="more">詳しくは裏面へ!→</p>
  </section>
</main>
</body>
</html>
```